Computer Company needs a Business card design

We need a business card design for our business. We assist people to transition to the QLX (Quorra Linkwave Exchange). The Australian Government-owned qlx™ network is a brand new telecommunications network currently being rolled out across Australia, giving access to a reliable broadband connection. Our niche market will predominantly be domestic customers in the 50+ age bracket. The assistance that we provide is everything from arranging the equipment, arranging the plan and contract term, appointment times, final testing of the network and any tweaks that need to be made. We basically PM the transition from start to finish. The business card design should be minimalist, should communicate loyalty and stability, should be easy to read and clearly explain what we do. We have asked for front and back. However, the back of the card does not have to include much information at all. It could be just a small design, or a repeat of our phone number. Up to you. The attached file only says what is required on the card. It does not specify where to arrange the text, what fonts to use, etc etc. As much as we would like to give you more info, due to our very limited design ability, we are not really able to send you any rough, or otherwise, designs of what we are after. Hopefully the above description is enough for you.

```html
<!DOCTYPE html>
<html lang="en">
<head>
<meta charset="utf-8">
<title>QLX Assist – Business Card</title>
<link rel="stylesheet" href="https://fonts.googleapis.com/css2?family=Quicksand:wght@400;500;700&display=swap">
<style>
  :root {
    --stage: #dcdcdc;
    --paper-light: #ffffff;
    --paper-shade: #d9d9d9;
    --brand-blue: #144e93;
    --brand-navy: #263f79;
    --logo-grey: #3b3b3d;
    --ink: #2b2b2b;
    --white: #ffffff;
  }
  html, body {
    margin: 0;
    padding: 0;
    width: 1200px;
    height: 718px;
    overflow: hidden;
    background: var(--stage);
    font-family: "Quicksand", sans-serif;
  }
  .canvas {
    position: relative;
    width: 1200px;
    height: 718px;
  }
  .card {
    position: absolute;
    top: 175px;
    width: 520px;
    height: 312px;
    box-shadow: 0 10px 18px rgba(0,0,0,0.25);
  }
  .card--front { left: 61px; }
  .card--back { left: 619px; }
  .card svg { display: block; width: 100%; height: 100%; }
  text { font-family: "Quicksand", sans-serif; }
  .logo-word { font-weight: 700; fill: var(--logo-grey); }
  .holder-first { font-weight: 700; fill: var(--white); }
  .holder-last { font-weight: 400; fill: var(--white); }
  .holder-role { font-weight: 700; fill: var(--white); }
  .contact-line { font-weight: 500; fill: var(--white); }
  .icon { fill: none; stroke: var(--white); stroke-width: 1.3; }
  .web-address { font-weight: 500; fill: var(--ink); }
</style>
</head>
<body>
<main class="canvas">

  <section class="card card--front" aria-label="Front of business card">
    <svg viewBox="0 0 540 324" xmlns="http://www.w3.org/2000/svg">
      <defs>
        <radialGradient id="paperFront" cx="0.2" cy="0.4" r="0.8">
          <stop offset="0" stop-color="var(--paper-light)"/>
          <stop offset="1" stop-color="var(--paper-shade)"/>
        </radialGradient>
      </defs>
      <rect class="paper" width="540" height="324" fill="url(#paperFront)"/>

      <path d="M0,0 L12,0 Q16,200 72,324 L0,324 Z" fill="var(--brand-navy)"/>
      <path d="M0,120 Q30,260 62,324 L0,324 Z" fill="var(--brand-blue)"/>
      <path d="M12,0 Q16,200 72,324" fill="none" stroke="var(--white)" stroke-width="3"/>

      <path d="M530,0 L540,0 L540,324 L232,324 Q240,40 530,0 Z" fill="var(--white)"/>
      <path d="M540,0 L540,324 L246,324 Q258,48 540,0 Z" fill="var(--brand-navy)"/>
      <path d="M540,50 L540,324 L248,324 Q262,110 540,50 Z" fill="var(--brand-blue)"/>

      <text class="logo-word" x="78" y="130" font-size="34">QLX Assist</text>

      <text x="498" y="150" font-size="19" text-anchor="end"><tspan class="holder-first">Reid </tspan><tspan class="holder-last">Callan</tspan></text>
      <text class="holder-role" x="497" y="167" font-size="11" text-anchor="end">Managing Director</text>

      <text class="contact-line" x="468" y="216" font-size="13" text-anchor="end">0412587930</text>
      <rect class="icon" x="484" y="201" width="12" height="20" rx="2"/>
      <line class="icon" x1="488" y1="218" x2="492" y2="218"/>

      <text class="contact-line" x="468" y="244" font-size="13" text-anchor="end">email@qlxassist.com</text>
      <circle class="icon" cx="490" cy="240" r="3"/>
      <path class="icon" d="M493,240 v2 a2,2 0 0 0 4,0 v-2 a7,7 0 1 0 -3,6"/>

      <text class="contact-line" x="468" y="271" font-size="13" text-anchor="end">Address Here</text>
      <path class="icon" d="M490,278 C484,271 483,268 483,265 a7,7 0 0 1 14,0 c0,3 -1,6 -7,13 Z"/>
      <circle class="icon" cx="490" cy="265" r="2.5"/>
    </svg>
  </section>

  <section class="card card--back" aria-label="Back of business card">
    <svg viewBox="0 0 540 324" xmlns="http://www.w3.org/2000/svg">
      <defs>
        <radialGradient id="paperBack" cx="0.35" cy="0.3" r="0.8">
          <stop offset="0" stop-color="var(--paper-light)"/>
          <stop offset="1" stop-color="var(--paper-shade)"/>
        </radialGradient>
      </defs>
      <rect class="paper" width="540" height="324" fill="var(--white)"/>

      <path d="M315,0 L540,0 L540,240 Q480,70 315,0 Z" fill="var(--brand-navy)"/>
      <path d="M350,0 L540,0 L540,185 Q490,55 350,0 Z" fill="var(--brand-blue)"/>

      <path d="M0,82 Q40,262 228,324 L0,324 Z" fill="var(--brand-navy)"/>
      <path d="M0,120 Q55,280 200,324 L0,324 Z" fill="var(--brand-blue)"/>

      <path d="M16,0 L305,0 Q500,80 522,324 L224,324 Q40,262 16,0 Z" fill="url(#paperBack)"/>

      <text class="logo-word" x="270" y="178" font-size="38" text-anchor="middle">QLX Assist</text>
      <text class="web-address" x="270" y="234" font-size="12" text-anchor="middle">www.qlxassist.com.au</text>
    </svg>
  </section>

</main>
</body>
</html>
```